依頼詳細
前回、ロゴデザインをしていただきましたので、
引き続きまして名刺のデザインをお願いしたいです。

突飛なデザインは望んでいません。
爽やかさと高級感を一体に出来れば理想的です。

ロゴのデータはai形式で添付しておきます。
名刺は役員3人分のデータがほしいです。
宜しくお願いします。
記載項目
表面:ロゴ、役職、氏名、会社所在地、会社電話、FAX
携帯電話番号、メールアドレス、WEBサイトURL
裏面:営業品目
・建物解体工事業一式
建設業許可
・茨城県知事許可(般-14)第61923号
産業廃棄物収集運搬許可
・茨城県知事 許可番号:00702950318
・栃木県知事 許可番号:00605950318
・群馬県知事 許可番号:00408950318
裏面のどこかにもロゴが入ると尚良いが、
バランス的に不必要なら除外
希望イメージ
シンプル 複雑
単色 カラフル
暗い 明るい
日常 高級
遊び心 厳粛
未来的 伝統的
女性的 男性的
希望する色
青系
納品ファイル
• 高解像度JPG (.jpg)
• イラストレーター形式 (.ai)
• PNG形式 (.png)
補足説明
すみませんが、名刺の向きは横向きが良いです。
よろしくお願いします。
■ 選んだ理由

解体業界という荒くれ者が集う業界という悪いイメージを払拭できるような爽やかさと実直さを兼ねたデザインという観点から選ばせていただきました。

■ 提案者全員のお礼・コメント

この度は弊社の名刺デザインコンペにご応募いただきまして、誠にありがとうございました。どのデザインも目を見張るものがありましたが、最終的には奇抜さよりも、シンプルかつ見やすさ・機能性の優れたデザインのものが良いだろうという結論に至りました。当選のデザイン・次点のデザインはもちろん、他の方々のデザインも私たちの意に沿う素晴らしいものでありました。また別の機会がありましたら是非とも宜しくお願い致します。

```html
<!DOCTYPE html>
<html lang="ja">
<head>
<meta charset="utf-8">
<title>上瀬解体工業 名刺デザイン</title>
<link href="https://fonts.googleapis.com/css2?family=Noto+Sans+JP:wght@400;500;700;900&display=swap" rel="stylesheet">
<style>
:root{
  --sheet:#eceeef;
  --blue:#1a78c8;
  --blue-deep:#0f5aa6;
  --blue-light:#4aa6e8;
  --ink:#333;
  --grey:#777;
  --line:#d5dbe0;
  --white:#fff;
}
*{margin:0;padding:0;box-sizing:border-box}
html,body{width:900px;height:1200px;overflow:hidden}
body{background:var(--sheet);font-family:"Noto Sans JP",sans-serif;color:var(--ink);position:relative}
.side-label{position:absolute;right:78px;font-size:15px;color:#555}
.side-label.front{top:22px}
.side-label.back{top:612px}
.card{position:absolute;left:75px;width:750px;box-shadow:0 3px 10px rgba(0,0,0,.25);overflow:hidden}
.card-front{top:51px;height:498px;background:linear-gradient(180deg,#fff 0%,#f6f7f8 100%)}
.card-back{top:645px;height:510px;background:linear-gradient(180deg,var(--blue-light) 0%,var(--blue) 45%,var(--blue-deep) 100%);color:var(--white)}
.faint-mark{position:absolute;right:-60px;top:40px;width:360px;height:360px;border-radius:50%;background:rgba(0,0,0,.035)}
.brand{position:absolute;display:flex;align-items:center;gap:12px;font-weight:900;letter-spacing:1px}
.brand-dot{border-radius:50%;display:block}
.card-front .brand{left:55px;top:38px;font-size:44px;color:var(--blue)}
.card-front .brand-dot{width:48px;height:48px;background:var(--blue)}
.rule{position:absolute;left:55px;right:0;top:120px;height:2px;background:linear-gradient(90deg,var(--blue) 0%,var(--line) 60%,transparent 100%)}
.role{position:absolute;left:60px;top:150px;font-size:15px;color:var(--grey)}
.name{position:absolute;left:58px;top:170px;font-size:42px;font-weight:500;letter-spacing:14px}
.name-roman{position:absolute;left:62px;top:232px;font-size:13px;color:var(--grey);letter-spacing:2px}
.contact{position:absolute;left:388px;display:flex;align-items:center;gap:8px;font-size:18px}
.contact svg{width:20px;height:20px}
.contact.mobile{top:160px}
.contact.mail{top:198px;font-size:17px}
.company{position:absolute;left:58px;top:278px;display:flex;align-items:center;gap:6px}
.company-name{font-size:30px;font-weight:900;letter-spacing:1px}
.company-type{font-size:11px;line-height:1.15;font-weight:700;width:26px}
.company-tag{position:absolute;left:60px;top:322px;font-size:14px;font-weight:500;color:#444}
.address{position:absolute;left:378px;top:284px;font-size:15px}
.tel-row{position:absolute;left:378px;top:318px;display:flex;gap:22px;font-size:16px}
.tel-row span{display:flex;align-items:center;gap:6px}
.tel-row svg{width:18px;height:18px}
.url-band{position:absolute;left:0;right:0;top:408px;height:44px;background:linear-gradient(90deg,#fff 0%,var(--blue-light) 35%,var(--blue) 100%);display:flex;align-items:center;justify-content:flex-end;padding-right:40px;gap:10px;color:var(--white);font-size:19px;letter-spacing:.5px}
.url-band svg{width:22px;height:22px}
.card-back .brand{left:465px;top:62px;font-size:40px;color:var(--white)}
.card-back .brand-dot{width:44px;height:44px;background:var(--white)}
.scope{position:absolute;left:40px;top:70px;font-size:18px}
.licence{position:absolute;left:40px;font-size:18px;line-height:33px}
.licence.building{top:142px}
.licence.waste{top:246px}
</style>
</head>
<body>
<div class="side-label front">design001：おもて面</div>
<section class="card card-front">
  <div class="faint-mark"></div>
  <div class="brand"><span class="brand-dot"></span>KAMISE</div>
  <div class="rule"></div>
  <div class="role">代表取締役</div>
  <div class="name">上瀬 誠</div>
  <div class="name-roman">Makoto Kamise</div>
  <div class="contact mobile">
    <svg viewBox="0 0 20 20"><rect x="5" y="1" width="10" height="18" rx="2" fill="none" stroke="#1a78c8" stroke-width="2"/><circle cx="10" cy="15.5" r="1.2" fill="#1a78c8"/></svg>
    090-4821-3370
  </div>
  <div class="contact mail">
    <svg viewBox="0 0 20 20"><rect x="1.5" y="4" width="17" height="12" fill="none" stroke="#1a78c8" stroke-width="2"/><path d="M2 5l8 6 8-6" fill="none" stroke="#1a78c8" stroke-width="2"/></svg>
    m.kamise@kamisekaitai.jp
  </div>
  <div class="company"><span class="company-name">上瀬解体工業</span><span class="company-type">株式会社</span></div>
  <div class="company-tag">茨城・栃木の総合解体工事業</div>
  <div class="address">〒308-0042 茨城県筑西市大字中舘412</div>
  <div class="tel-row">
    <span><svg viewBox="0 0 20 20"><rect width="20" height="20" rx="3" fill="#1a78c8"/><path d="M6 4l3 3-1.5 2a8 8 0 0 0 3.5 3.5L13 11l3 3-2 2C9 15 5 11 4 6z" fill="#fff"/></svg>0296-58-2190</span>
    <span><svg viewBox="0 0 20 20"><rect width="20" height="20" rx="3" fill="#1a78c8"/><rect x="5" y="8" width="10" height="7" fill="#fff"/><rect x="7" y="4" width="6" height="4" fill="#fff"/></svg>0296-58-2191</span>
  </div>
  <div class="url-band">
    <svg viewBox="0 0 22 22"><circle cx="11" cy="11" r="9" fill="none" stroke="#fff" stroke-width="1.8"/><ellipse cx="11" cy="11" rx="4" ry="9" fill="none" stroke="#fff" stroke-width="1.5"/><path d="M2 11h18M4 6h14M4 16h14" stroke="#fff" stroke-width="1.3"/></svg>
    http://www.kamisekaitai.jp
  </div>
</section>

<div class="side-label back">design001：うら面</div>
<section class="card card-back">
  <div class="scope">建物解体工事業一式</div>
  <div class="brand"><span class="brand-dot"></span>KAMISE</div>
  <div class="licence building">【建設業許可】<br>茨城県知事許可（般-14）第61923号</div>
  <div class="licence waste">【産業廃棄物収集運搬許可】<br>茨城県知事　許可番号：00702950318<br>栃木県知事　許可番号：00605950318<br>群馬県知事　許可番号：00408950318</div>
</section>
</body>
</html>
```